TORVEN RENEWABLES

New business B2B Energy Renewables website.
Please refer to our competitor https://www.quorbit72.co.uk/ for a similar website.

Need extra days to review

```html
<!DOCTYPE html>
<html lang="en">
<head>
<meta charset="utf-8">
<title>Torven Renewables</title>
<link href="https://fonts.googleapis.com/css2?family=Josefin+Sans:wght@400;600;700&family=Lato:wght@400;700&display=swap" rel="stylesheet">
<style>
:root{
  --blue:#1f6bff;
  --blue-deep:#0f3ea8;
  --navy:#0a1b4d;
  --ink:#111111;
  --text:#3a3a3a;
  --pale:#eaf1fb;
  --white:#ffffff;
  --footer:#0c1226;
}
*{box-sizing:border-box;margin:0;padding:0}
html,body{width:1200px;height:3555px;overflow:hidden;background:var(--white)}
body{font-family:'Lato',sans-serif;color:var(--text)}
.page{position:relative;width:1200px;height:3555px;overflow:hidden}
.abs{position:absolute}
.head{font-family:'Josefin Sans',sans-serif}
.btn{position:absolute;display:flex;align-items:center;justify-content:center;font-family:'Josefin Sans',sans-serif;font-weight:700;font-size:15px;border-radius:22px 4px 22px 4px}
.btn-blue{background:linear-gradient(90deg,var(--blue-deep),var(--blue));color:var(--white)}
.btn-white{background:var(--white);color:var(--blue)}
.eyebrow{position:absolute;font-family:'Josefin Sans',sans-serif;font-weight:600;font-size:15px;color:var(--blue)}
.title{position:absolute;font-family:'Josefin Sans',sans-serif;font-weight:600;font-size:35px;color:var(--ink)}
.body{position:absolute;font-size:15px;line-height:25.7px;color:var(--text)}
.more{font-family:'Josefin Sans',sans-serif;font-weight:700;font-size:15px;color:var(--blue);display:flex;align-items:center;gap:8px}

.topbar{left:0;top:0;width:1200px;height:43px;background:linear-gradient(90deg,#1b4fc6,#1f6bff)}
.topbar .call{left:158px;top:12px;color:var(--white);font-size:15px;font-weight:700;display:flex;gap:8px;align-items:center}
.social{top:6px;width:31px;height:31px;border-radius:50%;background:var(--white)}
.quote{left:929px;top:12px;color:var(--white);font-family:'Josefin Sans',sans-serif;font-weight:600;font-size:16px;display:flex;gap:7px;align-items:center}
.logo-tab{left:459px;top:0;width:238px;height:43px;background:var(--white);clip-path:polygon(0 0,100% 0,86% 100%,14% 100%)}
.nav{left:0;top:43px;width:1200px;height:65px;background:var(--white)}
.nav a{position:absolute;top:24px;font-family:'Josefin Sans',sans-serif;font-weight:600;font-size:15px;color:var(--ink);text-decoration:none}
.brand{left:480px;top:22px;width:240px;height:72px;display:flex;align-items:center;justify-content:center;gap:8px;font-family:'Josefin Sans',sans-serif;font-weight:700;font-size:18px;color:var(--navy);letter-spacing:1px}
.brand i{display:block;width:16px;height:16px;background:var(--blue-deep)}

.hero-band-cut{left:0;top:108px;width:1089px;height:619px;background:linear-gradient(90deg,#123f9e,#1f6bff);border-bottom-left-radius:150px;clip-path:polygon(0 0,100% 0,100% 97%,98% 100%,0 100%)}
.hero-photo{left:0;top:108px;width:1200px;height:600px;border-bottom-left-radius:140px;background:linear-gradient(180deg,#6f86b5 0%,#3c5a99 40%,#1e3a7c 70%,#14264f 100%)}
.hero h1{position:absolute;left:112px;top:264px;font-family:'Josefin Sans',sans-serif;font-weight:600;font-size:44px;line-height:51px;color:var(--white)}
.hero p{position:absolute;left:112px;top:380px;width:520px;font-size:15px;line-height:25px;color:#e7ecf7}

.services-bg{left:0;top:708px;width:1200px;height:730px;background:var(--pale)}
.card{position:absolute;width:230px;height:265px;background:var(--white);border-radius:4px;box-shadow:0 6px 20px rgba(20,50,120,.08)}
.card .ico{position:absolute;left:12px;top:25px;width:53px;height:53px;border-radius:50%;background:linear-gradient(135deg,#1f6bff,#0f3ea8)}
.card h3{position:absolute;left:17px;top:98px;font-family:'Josefin Sans',sans-serif;font-weight:600;font-size:21px;color:var(--ink)}
.card p{position:absolute;left:17px;top:134px;width:200px;font-size:15px;line-height:25.7px}
.card .more{position:absolute;left:19px;top:222px}
.card.active{background:linear-gradient(160deg,#0f3ea8,#1f6bff)}
.card.active .ico{background:var(--white)}
.card.active h3,.card.active p,.card.active .more{color:var(--white)}

.sol{position:absolute;top:1620px;width:309px;height:462px;border-radius:8px;background:var(--white)}
.sol.raised{box-shadow:0 6px 26px rgba(0,0,0,.12)}
.sol .img{position:absolute;left:0;top:0;width:309px;height:225px;border-radius:8px 8px 0 0}
.sol .tag{position:absolute;left:13px;top:214px;width:54px;height:52px;background:var(--blue);border-radius:3px}
.sol h3{position:absolute;left:84px;top:235px;width:215px;font-family:'Josefin Sans',sans-serif;font-weight:600;font-size:21px;line-height:26px;color:var(--ink)}
.sol p{position:absolute;left:15px;width:280px;font-size:15px;line-height:25.7px}
.sol .more{position:absolute;left:17px;top:418px}

.about{left:0;top:2163px;width:1200px;height:450px;background:linear-gradient(90deg,#123783 0%,#1c4aa3 45%,#3a63b0 75%,#506fa8 100%)}
.about .eyebrow{color:var(--white)}
.about .title{color:var(--white)}
.about .body{color:#e3e9f6}

.form{left:509px;top:2699px;width:576px;height:368px;background:var(--white);border-radius:4px;box-shadow:0 6px 26px rgba(0,0,0,.08)}
.field{position:absolute;border:1px solid #b9bec8;border-radius:2px;font-size:15px;color:#777;padding:9px 14px}
.info{position:absolute;left:112px;display:flex;align-items:center;gap:14px;font-size:15px;line-height:25px;color:var(--text)}

.foot-band{left:0;top:3145px;width:1200px;height:410px;background:var(--blue);clip-path:polygon(112px 0,1090px 0,1200px 60px,1200px 100%,0 100%,0 0)}
.foot{left:0;top:3166px;width:1200px;height:389px;background:var(--footer);border-top-right-radius:110px}
.foot h4{position:absolute;top:3236px;font-family:'Josefin Sans',sans-serif;font-weight:600;font-size:19px;color:var(--white)}
.foot-links{position:absolute;top:3278px;font-size:15px;line-height:30px;color:#e6e9f0;list-style:none}
.foot-brand{left:112px;top:3262px;font-family:'Josefin Sans',sans-serif;font-weight:700;font-size:20px;letter-spacing:1px;color:var(--white);display:flex;align-items:center;gap:8px}
.foot-brand i{display:block;width:16px;height:16px;background:var(--white)}
.dot{position:absolute;top:3353px;width:12px;height:12px;border-radius:50%;background:var(--blue)}
</style>
</head>
<body>
<div class="page">

  <div class="abs topbar">
    <div class="abs call">
      <svg width="16" height="16" viewBox="0 0 24 24" fill="#fff"><path d="M6.6 10.8a15.1 15.1 0 006.6 6.6l2.2-2.2a1 1 0 011-.25 11.4 11.4 0 003.6.57 1 1 0 011 1V20a1 1 0 01-1 1A17 17 0 013 4a1 1 0 011-1h3.5a1 1 0 011 1c0 1.25.2 2.45.57 3.57a1 1 0 01-.25 1z"/></svg>
      Call Us+1 555 014 2277
    </div>
    <div class="abs social" style="left:782px"></div>
    <div class="abs social" style="left:821px"></div>
    <div class="abs social" style="left:859px"></div>
    <div class="abs quote">
      <svg width="12" height="15" viewBox="0 0 12 15" fill="#fff"><path d="M0 0h8l4 4v11H0z"/></svg>
      Free Quote
    </div>
  </div>
  <div class="abs logo-tab"></div>
  <nav class="abs nav">
    <a style="left:141px">Home</a>
    <a style="left:248px">About Us</a>
    <a style="left:379px">Services</a>
    <a style="left:748px">Renewable Solutions</a>
    <a style="left:953px">Contact Us</a>
  </nav>
  <div class="abs brand"><i></i>TORVEN RENEWABLES</div>

  <section class="hero">
    <div class="abs hero-band-cut"></div>
    <div class="abs hero-photo" role="img" aria-label="Wind turbines, solar panels and an energy storage container in a grassy field at dusk, tinted blue"></div>
    <h1>Welcome To<br>Torven Renewables</h1>
    <p>Lorem ipsum dolor sit amet, consectetur adipiscing elit, sed do eiusmod tempor incididunt ut labore et dolore magna aliqua.</p>
    <div class="btn btn-blue" style="left:112px;top:455px;width:150px;height:50px">Get Started</div>
  </section>

  <section>
    <div class="abs services-bg"></div>
    <div class="eyebrow" style="left:113px;top:890px">How it Work</div>
    <div class="title" style="left:112px;top:914px">Our Services</div>
    <p class="body" style="left:112px;top:964px;width:422px">Lorem ipsum dolor sit amet, consectetur adipiscing elit, sed do eiusmod tempor incididunt ut labore et dolore magna aliqua. Quis ipsum suspendisse ultrices gravida. Risus commodo viverra maecenas accumsan lacus vel facilisis. Lorem ipsum dolor sit amet, consectetur adipiscing elit, sed do eiusmod tempor incididunt ut labore et dolore magna aliqua. Quis ipsum suspendisse ultrices gravida. Risus commodo viverra maecenas accumsan lacus vel facilisis. Lorem ipsum dolor sit amet</p>
    <div class="btn btn-blue" style="left:112px;top:1217px;width:152px;height:50px">Learn More</div>

    <div class="card active" style="left:600px;top:963px">
      <div class="ico"></div>
      <h3>Design</h3>
      <p>Lorem ipsum dolor sit amet, consectetur adipiscing elit, sed do eiusmod tempor.</p>
      <div class="more">Learn More <svg width="14" height="14" viewBox="0 0 14 14"><circle cx="7" cy="7" r="7" fill="#fff"/><path d="M5 4l3 3-3 3" stroke="#1f6bff" stroke-width="1.8" fill="none"/></svg></div>
    </div>
    <div class="card" style="left:859px;top:800px">
      <div class="ico"></div>
      <h3>Consulting</h3>
      <p>Lorem ipsum dolor sit amet, consectetur adipiscing elit, sed do eiusmod tempor.</p>
      <div class="more">Learn More <svg width="14" height="14" viewBox="0 0 14 14"><circle cx="7" cy="7" r="7" fill="#1f6bff"/><path d="M5 4l3 3-3 3" stroke="#fff" stroke-width="1.8" fill="none"/></svg></div>
    </div>
    <div class="card" style="left:859px;top:1094px">
      <div class="ico"></div>
      <h3>Finance</h3>
      <p>Lorem ipsum dolor sit amet, consectetur adipiscing elit, sed do eiusmod tempor.</p>
      <div class="more">Learn More <svg width="14" height="14" viewBox="0 0 14 14"><circle cx="7" cy="7" r="7" fill="#1f6bff"/><path d="M5 4l3 3-3 3" stroke="#fff" stroke-width="1.8" fill="none"/></svg></div>
    </div>
  </section>

  <section>
    <div class="eyebrow" style="left:0;width:1200px;text-align:center;top:1516px">Our Solutions</div>
    <div class="title" style="left:0;width:1200px;text-align:center;top:1538px">Renewable Solutions</div>

    <div class="sol" style="left:112px">
      <div class="img" role="img" aria-label="Rows of solar panels under a cloudy sky" style="background:linear-gradient(180deg,#7fa6c8 0%,#c9d6df 40%,#55606e 60%,#2a3340 100%)"></div>
      <div class="tag"></div>
      <h3>Various renewables offered</h3>
      <p style="top:300px">Lorem ipsum dolor sit amet, consectetur adipiscing elit, sed do eiusmod tempor incididunt ut labore et dolore magna aliqua.</p>
      <div class="more">Learn More <svg width="14" height="14" viewBox="0 0 14 14"><circle cx="7" cy="7" r="7" fill="#1f6bff"/><path d="M5 4l3 3-3 3" stroke="#fff" stroke-width="1.8" fill="none"/></svg></div>
    </div>
    <div class="sol raised" style="left:445px">
      <div class="img" role="img" aria-label="Wind turbines on green fields at sunset" style="background:linear-gradient(180deg,#3a5f9a 0%,#e3a33f 40%,#6f8a3a 65%,#3f6a2a 100%)"></div>
      <div class="tag"></div>
      <h3>Energy Saving Assessment</h3>
      <p style="top:300px">Lorem ipsum dolor sit amet, consectetur adipiscing elit, sed do eiusmod tempor incididunt ut labore et dolore magna aliqua.</p>
      <div class="more">Learn More <svg width="14" height="14" viewBox="0 0 14 14"><circle cx="7" cy="7" r="7" fill="#1f6bff"/><path d="M5 4l3 3-3 3" stroke="#fff" stroke-width="1.8" fill="none"/></svg></div>
    </div>
    <div class="sol" style="left:779px">
      <div class="img" role="img" aria-label="Operator at a desk watching monitoring screens" style="background:linear-gradient(90deg,#c9ccd3 0%,#8a93a6 45%,#2b3f6a 70%,#1a2a4a 100%)"></div>
      <div class="tag"></div>
      <h3 style="top:244px">Monitoring</h3>
      <p style="top:275px">Lorem ipsum dolor sit amet, consectetur adipiscing elit, sed do eiusmod tempor incididunt ut labore dolore magna aliqua. Quis ipsum suspendisse ultrices gravida.</p>
      <div class="more">Learn More <svg width="14" height="14" viewBox="0 0 14 14"><circle cx="7" cy="7" r="7" fill="#1f6bff"/><path d="M5 4l3 3-3 3" stroke="#fff" stroke-width="1.8" fill="none"/></svg></div>
    </div>
  </section>

  <section class="abs about" role="img" aria-label="Solar panel rows and wind turbines beside storage units, blue tinted">
    <div class="eyebrow" style="left:112px;top:61px;font-size:15px">Welcome To Torven Renewables</div>
    <div class="title" style="left:112px;top:82px">About Torven Renewables</div>
    <p class="body" style="left:112px;top:138px;width:480px">Lorem ipsum dolor sit amet, consectetur adipiscing elit, sed do eiusmod tempor incididunt ut labore et dolore magna aliqua. Quis ipsum suspendisse ultrices gravida. Risus commodo viverra maecenas accumsan lacus vel facilisis. Lorem ipsum dolor sit amet, consectetur adipiscing elit, sed do eiusmod tempor incididunt ut labore et dolore magna aliqua. Quis ipsum suspendisse ultrices gravida. Risus commodo viverra maecenas accumsan</p>
    <div class="btn btn-white" style="left:112px;top:342px;width:150px;height:50px">Learn More</div>
  </section>

  <section>
    <div class="eyebrow" style="left:111px;top:2702px">Get A Quote</div>
    <div class="title" style="left:110px;top:2724px">Contact Us</div>
    <p class="body" style="left:111px;top:2782px;width:365px">Lorem ipsum dolor sit amet, consectetur adipiscing elit, sed do eiusmod tempor incididunt ut labore et dolore magna aliqua. Quis ipsum suspendisse ultrices gravida. Risus commodo</p>
    <div class="info" style="top:2906px">
      <svg width="28" height="34" viewBox="0 0 28 34"><path d="M14 2a11 11 0 00-11 11c0 8 11 19 11 19s11-11 11-19A11 11 0 0014 2z" fill="none" stroke="#1f6bff" stroke-width="1.8"/><circle cx="14" cy="13" r="4" fill="none" stroke="#1f6bff" stroke-width="1.8"/></svg>
      <span>Lorem ipsum dolor sit amet,<br>consectetur adipiscing elit, sed do</span>
    </div>
    <div class="info" style="top:2985px">
      <svg width="32" height="30" viewBox="0 0 24 24"><path d="M6.6 10.8a15.1 15.1 0 006.6 6.6l2.2-2.2a1 1 0 011-.25 11.4 11.4 0 003.6.57 1 1 0 011 1V20a1 1 0 01-1 1A17 17 0 013 4a1 1 0 011-1h3.5a1 1 0 011 1c0 1.25.2 2.45.57 3.57a1 1 0 01-.25 1z" fill="none" stroke="#1f6bff" stroke-width="1.3"/></svg>
      <span>+1 555 014 2277</span>
    </div>
    <div class="info" style="top:3044px">
      <svg width="32" height="24" viewBox="0 0 32 24"><rect x="1" y="1" width="30" height="22" fill="none" stroke="#1f6bff" stroke-width="1.8"/><path d="M1 1l15 12L31 1" fill="none" stroke="#1f6bff" stroke-width="1.8"/></svg>
      <span style="color:var(--blue)">info@torvenrenewables.com</span>
    </div>

    <div class="abs form">
      <div class="abs head" style="left:32px;top:40px;font-weight:600;font-size:23px;color:var(--ink)">Get A Quote</div>
      <div class="field" style="left:32px;top:92px;width:242px;height:42px">Name</div>
      <div class="field" style="left:32px;top:156px;width:242px;height:42px">Email</div>
      <div class="field" style="left:32px;top:219px;width:242px;height:42px">Phone</div>
      <div class="field" style="left:301px;top:92px;width:242px;height:169px">Type Your Message</div>
      <div class="abs head" style="left:32px;top:284px;width:510px;height:41px;background:var(--blue);color:#fff;font-weight:600;font-size:15px;display:flex;align-items:center;justify-content:center">Send Message</div>
    </div>
  </section>

  <footer>
    <div class="abs foot-band"></div>
    <div class="abs foot"></div>
    <div class="abs foot-brand"><i></i>TORVEN<br>RENEWABLES</div>
    <div class="dot" style="left:184px"></div>
    <div class="dot" style="left:209px"></div>
    <div class="dot" style="left:234px"></div>
    <div class="dot" style="left:260px"></div>

    <h4 style="left:361px">Quick Link</h4>
    <ul class="foot-links" style="left:364px"><li>Home</li><li>About Us</li><li>Our Services</li><li>Renewable Solutions</li><li>Contact Us</li></ul>
    <h4 style="left:541px">Services</h4>
    <ul class="foot-links" style="left:545px"><li>Consulting</li><li>Design</li><li>Finance</li><li>Installation</li><li>Maintenance</li></ul>
    <h4 style="left:677px">Support</h4>
    <ul class="foot-links" style="left:680px"><li>Terms&amp;condtions</li><li>Privacy Policy</li><li>About Us</li><li>Support</li></ul>
    <h4 style="left:843px">Subscribe To Our Newsletter</h4>
    <div class="abs" style="left:846px;top:3280px;width:241px;height:30px;border-bottom:1px solid #39415a;border-left:2px solid #fff;padding-left:12px;font-size:14px;color:#4a5068;line-height:30px">Enter Your Email</div>
    <div class="btn btn-blue" style="left:844px;top:3339px;width:120px;height:34px;border-radius:17px;font-size:15px">Subscribe</div>

    <div class="abs" style="left:112px;top:3464px;width:976px;height:1px;background:#232a40"></div>
    <div class="abs" style="left:0;top:3494px;width:1200px;text-align:center;font-size:15px;color:#e6e9f0">©Copyrights 2022 Torven Renewables &nbsp;|&nbsp;&nbsp; All Rights Reserved</div>
  </footer>
</div>
</body>
</html>
```